Stationery for use with Ninefold Ridge reports

I would like to get a stationery design that my firm -- Ninefold Ridge Advisory -- will use as a format for reports that we send our clients. I am specifically looking for a design for use on a piece of paper or letterhead -- not business cards or envelopes.

We are an Africa based US risk intelligence and strategy firm that works with multinational corporations operating in West Africa. Our initial thinking is that we would like a color scheme consistent with our existing logo -- however we are open to other color schemes.

Also, we would like to see at least two separate versions: one with our company name and logo, the other without name and logo.

We also would like font recommendations for the stationary design.

The final design should communicate discreet professionalism and a modern approach, but it should not overshadow the words and information printed on the stationery.

Target Market(s)

Multinational corporations that currently use our products.

Font styles to use
Serif
Sans Serif

Requirements
Must have
• Sense of discreet professionalism that will not overshadow the content we put onto the stationery format.
• We would like to see designs with and without our company name/logo.
• Please suggest fonts that would work with the stationery.
Nice to have
• Ideally colors consistent with out existing logo, though we are open to and even encourage other ideas.
Should not have
• No need for business cards or envelopes.

```html
<!DOCTYPE html>
<html lang="en">
<head>
<meta charset="utf-8">
<title>Ninefold Ridge Advisory — Letterhead</title>
<link href="https://fonts.googleapis.com/css2?family=Montserrat:wght@700&family=Lato:wght@400&display=swap" rel="stylesheet">
<style>
  :root {
    --backdrop: #cbbfbb;
    --paper: #fdfcf8;
    --navy: #1f3d4f;
    --gold: #e0a23c;
    --ink: #2b3a45;
  }
  * { margin: 0; padding: 0; box-sizing: border-box; }
  html, body {
    width: 1200px;
    height: 784px;
    overflow: hidden;
    background: var(--backdrop);
  }
  .letterhead {
    position: absolute;
    left: 314px;
    top: 22px;
    width: 572px;
    height: 740px;
    background: var(--paper);
    box-shadow: 0 2px 6px rgba(0,0,0,0.12);
  }
  .edge-band {
    position: absolute;
    left: 0;
    top: 0;
    width: 12px;
    height: 100%;
  }
  .wordmark {
    position: absolute;
    top: 46px;
    right: 56px;
    text-align: right;
    font-family: "Montserrat", sans-serif;
    font-weight: 700;
    color: var(--navy);
    line-height: 1.1;
  }
  .wordmark .name { font-size: 24px; letter-spacing: 0.5px; display: block; }
  .wordmark .descriptor { font-size: 11px; letter-spacing: 4px; display: block; margin-top: 4px; }
  .contact {
    position: absolute;
    top: 300px;
    right: 40px;
    padding-left: 12px;
    border-left: 1px solid var(--gold);
    font-family: "Lato", sans-serif;
    font-size: 9.5px;
    color: var(--ink);
    line-height: 1.55;
  }
  .contact .line { display: flex; align-items: center; gap: 5px; }
  .contact svg { width: 8px; height: 8px; flex: none; }
  .contact .address { padding-left: 13px; }
  .corner-mark {
    position: absolute;
    left: 48px;
    bottom: 46px;
    width: 34px;
    height: 34px;
    border-radius: 50%;
    background: var(--gold);
  }
</style>
</head>
<body>
  <main class="letterhead">
    <svg class="edge-band" viewBox="0 0 12 740" preserveAspectRatio="none" aria-hidden="true">
      <polygon points="0,0 12,0 12,330 0,338" fill="var(--gold)"/>
      <polygon points="0,344 12,336 12,740 0,740" fill="var(--navy)"/>
    </svg>

    <header class="wordmark">
      <span class="name">Ninefold Ridge</span>
      <span class="descriptor">ADVISORY</span>
    </header>

    <address class="contact" style="font-style:normal">
      <div class="address">1234 First Line Address</div>
      <div class="address">5678 Second Line Address</div>
      <div class="line">
        <svg viewBox="0 0 10 10"><path d="M2 1l2 2-1 1.2c.6 1.2 1.5 2.1 2.8 2.8L7 6l2 2-1.3 1.3C4.5 9 1 5.5.7 2.3z" fill="var(--gold)"/></svg>
        (111) 999-0000
      </div>
      <div class="line">
        <svg viewBox="0 0 10 10"><rect x="0.5" y="2" width="9" height="6" fill="var(--gold)"/><path d="M0.5 2l4.5 3.5L9.5 2" stroke="var(--paper)" stroke-width="0.9" fill="none"/></svg>
        info@ninefoldridge.com
      </div>
      <div class="line">
        <svg viewBox="0 0 10 10"><circle cx="5" cy="5" r="4.3" fill="none" stroke="var(--gold)" stroke-width="1"/><path d="M0.7 5h8.6M5 .7c-2 2.4-2 6.2 0 8.6M5 .7c2 2.4 2 6.2 0 8.6" stroke="var(--gold)" stroke-width="0.7" fill="none"/></svg>
        www.ninefoldridge.com
      </div>
    </address>

    <div class="corner-mark" aria-hidden="true"></div>
  </main>
</body>
</html>
```